Have Logo - Need Business Card Design!!!

I am looking for a business card design for a real estate development business. The company name is Quillmont Realty Partners. I already have a logo created by Sketch Harbor and would like this logo to be incorporated into the design. I have uploaded the files. The card needs to be professional, but visually interesting. Not necessary to be double-sided, but if you want to get creative and can think of something to put on the back then have at it.

Target Market(s)

The target audience for these business cards will be professionals in the real estate industry.

Industry/Entity Type

Real Estate

Requirements
Must have
• The business card must have all the necessary items for a business card, i.e. company name, our logo, name (however, not title necessary), office address, office phone number, cell number, fax number, website address, etc.

You can use the information below for the card:

Gregory L. Hanlon
782 Marlowe Avenue
San Francisco, California 94127

www.quillmontrealty.example
ghanlon@quillmontrealty.example
Office: 415-555-0142
Fax: 415-555-0143
Cell: 415-555-0186

```html
<!DOCTYPE html>
<html lang="en">
<head>
<meta charset="utf-8">
<title>Quillmont Realty Partners – Business Card</title>
<link rel="stylesheet" href="https://fonts.googleapis.com/css2?family=Exo+2:wght@400;500&display=swap">
<style>
  :root {
    --stage: #5f6063;
    --brand-green: #008a4b;
    --name-green: #14a055;
    --card-light: #e8e9eb;
    --band-blue: #384b7c;
    --label-blue: #5a6fa0;
    --text-grey: #4a4b4f;
    --muted-grey: #7d7e83;
    --white: #ffffff;
  }
  * { margin: 0; padding: 0; box-sizing: border-box; }
  html, body {
    width: 1200px; height: 895px; overflow: hidden;
    background: var(--stage);
    font-family: "Exo 2", Arial, sans-serif;
  }
  .canvas { position: relative; width: 1200px; height: 895px; }

  .card {
    position: absolute; width: 376px; height: 206px;
    border-radius: 14px; overflow: hidden;
  }

  /* Front */
  .card-front { left: 129px; top: 314px; background: var(--brand-green); }
  .front-mark {
    position: absolute; left: 0; right: 0; top: 80px;
    display: flex; align-items: center; justify-content: center; gap: 10px;
    color: rgba(255,255,255,0.22);
    font-size: 20px; font-weight: 400; letter-spacing: 0.5px;
    white-space: nowrap;
  }
  .front-mark .mark-square {
    width: 40px; height: 40px; background: rgba(255,255,255,0.12);
  }

  /* Back */
  .card-back { left: 631px; top: 315px; background: var(--card-light); }
  .back-logo {
    position: absolute; right: 20px; top: 25px;
    display: flex; align-items: center; gap: 6px;
    color: var(--brand-green); font-size: 14px; font-weight: 500;
    white-space: nowrap;
  }
  .back-logo .mark-square { width: 14px; height: 14px; background: var(--band-blue); }

  .holder { position: absolute; left: 25px; top: 74px; width: 140px; }
  .holder-name { color: var(--name-green); font-size: 16px; line-height: 18px; white-space: nowrap; }
  .holder-title { color: var(--muted-grey); font-size: 9px; text-align: right; line-height: 11px; }

  .contact {
    position: absolute; left: 189px; top: 102px;
    list-style: none; color: var(--text-grey);
    font-size: 9px; line-height: 12px; white-space: nowrap;
  }
  .contact .label { color: var(--label-blue); }
  .contact .indent { padding-left: 41px; }

  .web-band {
    position: absolute; left: 0; right: 0; bottom: 0; height: 24px;
    background: var(--band-blue); color: var(--white);
    font-size: 14px; letter-spacing: 0.6px;
    display: flex; align-items: center; justify-content: center;
    white-space: nowrap;
  }
</style>
</head>
<body>
<main class="canvas">
  <section class="card card-front" aria-label="Card front">
    <div class="front-mark">
      <span class="mark-square"></span>
      <span>Quillmont Realty Partners</span>
    </div>
  </section>

  <section class="card card-back" aria-label="Card back">
    <div class="back-logo">
      <span class="mark-square"></span>
      <span>Quillmont Realty Partners</span>
    </div>

    <div class="holder">
      <p class="holder-name">Gregory L. Hanlon</p>
      <p class="holder-title">President</p>
    </div>

    <ul class="contact">
      <li><span class="label">A:</span> 782 Marlowe Avenue</li>
      <li class="indent">San Francisco, California 94127</li>
      <li><span class="label">P#</span> 415-555-0142</li>
      <li><span class="label">C#</span> 415-555-0186</li>
      <li><span class="label">F#</span> 415-555-0143</li>
      <li><span class="label">E:</span> ghanlon@quillmontrealty.example</li>
    </ul>

    <div class="web-band">www.quillmontrealty.example</div>
  </section>
</main>
</body>
</html>
```